Email Sig, Letterhead, Business Card Design

Need a stationary package including email signature, letterhead/envelope, and business card design incorporating our new logo.

```html
<!DOCTYPE html>
<html lang="en">
<head>
<meta charset="utf-8">
<title>Corvell Engineering Stationery</title>
<link href="https://fonts.googleapis.com/css2?family=Open+Sans:wght@400;600&family=Roboto:wght@400;500;700&family=Roboto+Condensed:wght@500;700&display=swap" rel="stylesheet">
<style>
:root{
  --bg:#e7e7e7;
  --paper:#f4f4f4;
  --orange:#e05a2b;
  --blue:#1f5f99;
  --ink:#4a4a4a;
  --faint:rgba(31,95,153,.07);
}
*{margin:0;padding:0;box-sizing:border-box}
html,body{width:1200px;height:941px;overflow:hidden;background:var(--bg)}
body{position:relative;font-family:"Open Sans",sans-serif;color:var(--ink)}
.piece{position:absolute;background:var(--paper);box-shadow:0 2px 6px rgba(0,0,0,.12);overflow:hidden}

/* shared brand lockup: sized by font-size on .brand */
.brand{position:absolute;width:max-content;text-align:center;line-height:1.15}
.wordmark{font-family:"Roboto Condensed",sans-serif;font-weight:700;font-size:1em;color:var(--orange);white-space:nowrap;line-height:1.05}
.tagline{font-family:"Roboto Condensed",sans-serif;font-weight:500;font-size:.36em;color:var(--blue);white-space:nowrap}
.reg{font-family:"Roboto Condensed",sans-serif;font-weight:500;font-size:.28em;color:var(--orange);letter-spacing:.15em;white-space:nowrap;display:flex;align-items:center;gap:.5em}
.reg::before,.reg::after{content:"";flex:1;height:1px;background:var(--orange)}
.company{color:var(--blue);font-family:"Roboto",sans-serif;font-weight:500}
.contact{font-family:"Roboto",sans-serif;line-height:1.35;white-space:nowrap}
.contact svg{vertical-align:-1px;margin-right:2px}
.ghost{position:absolute;border-radius:50%;background:var(--faint)}

/* letterhead */
.letterhead{left:292px;top:105px;width:293px;height:414px}
.letterhead .brand{left:31px;top:52px;font-size:7.3px}
.letterhead .sender{position:absolute;left:200px;top:26px;font-size:4.6px;line-height:1.3}
.letterhead .letter{position:absolute;left:31px;top:104px;width:232px;font-size:5.1px;line-height:7.6px;text-align:justify}
.letterhead .letter p{margin-bottom:4.2px}
.letterhead .signature{position:absolute;left:33px;top:302px}

/* folder */
.folder{left:636px;top:85px;width:346px;height:437px}
.folder .spine{position:absolute;left:4px;top:0;bottom:0;width:10px;border-left:1px solid #d8d8d8;border-right:1px solid #d8d8d8}
.folder .brand{left:50%;transform:translateX(-50%);top:80px;font-size:14px}
.folder .photo{position:absolute;left:0;top:128px;width:346px;height:219px;background:linear-gradient(120deg,#b9a79a 0%,#a9694b 45%,#d4612b 65%,#5d6670 100%)}
.folder .footer{position:absolute;left:0;right:0;top:377px;text-align:center;font-family:"Roboto",sans-serif;font-size:8.2px;line-height:1.15}

/* business cards */
.card-back{left:186px;top:556px;width:133px;height:74px;background:var(--blue);box-shadow:none}
.card-back .pattern{position:absolute;inset:0;background:linear-gradient(135deg,#2a679f,#1c5790)}
.card-back .brand{left:63px;top:51px;font-size:5.2px}
.card-back .wordmark{color:#fff}
.card-front{left:186px;top:652px;width:133px;height:75px}
.card-front .brand{left:13px;top:43px;font-size:5px}
.card-front .rule{position:absolute;left:66px;top:18px;width:1px;height:40px;background:#777}
.card-front .details{position:absolute;left:72px;top:17px;font-size:3.3px;line-height:1.3}
.card-front .name{font-family:"Roboto",sans-serif;font-weight:700;color:var(--blue);font-size:4.1px}
.card-front .role{color:var(--orange);font-weight:600}

/* envelopes */
.envelope-front{left:353px;top:567px;width:328px;height:156px}
.envelope-front .brand{left:52px;transform:translateX(-50%);top:41px;font-size:7.3px}
.envelope-front .sender{position:absolute;left:0;width:104px;top:62px;text-align:center;font-size:5.3px;line-height:1.25}
.envelope-back{left:713px;top:567px;width:328px;height:156px}
.envelope-back .flap{position:absolute;left:0;top:0;width:328px;height:56px}
.envelope-back .brand{left:50%;transform:translateX(-50%);top:32px;font-size:6.3px}
.envelope-back .wordmark,.envelope-back .tagline{color:#fff}

/* email signature */
.email-sig{left:464px;top:754px;width:289px;height:96px;background:#fff;box-shadow:0 1px 4px rgba(0,0,0,.25)}
.email-sig .brand{left:18px;top:11px;font-size:11.5px;text-align:left}
.email-sig .person{position:absolute;left:145px;top:11px;font-family:"Roboto",sans-serif;line-height:1.15}
.email-sig .person .name{color:var(--orange);font-weight:700;font-size:9px}
.email-sig .person .role{color:var(--blue);font-weight:500;font-size:8.3px}
.email-sig .contact-list{position:absolute;left:18px;top:59px;font-size:7px}
.email-sig .office{position:absolute;left:145px;top:63px;font-size:6.7px;line-height:1.2;font-family:"Roboto",sans-serif}
</style>
</head>
<body>

<!-- letterhead -->
<section class="piece letterhead">
  <div class="ghost" style="left:190px;top:300px;width:110px;height:110px"></div>
  <div class="brand">
    <div class="wordmark">CORVELL ENGINEERING</div>
    <div class="tagline">1420 BRAMBLE RIDGE ROAD, CEDAR FALLS, TEXAS 77000</div>
    <div class="reg">STATE FIRM REGISTRATION F-0412</div>
  </div>
  <div class="sender contact">
    <div class="company">Corvell Engineering Ltd.</div>
    <div>Unit 12/48 Harlow Lane</div>
    <div>Brunswick, Victoria Australia</div>
    <div style="margin-top:3px"><svg width="4" height="4" viewBox="0 0 10 10"><path d="M2 1l2 2-1 2 2 2 2-1 2 2-2 2C4 10 0 6 0 3z" fill="#e05a2b"/></svg>+61 3 9000 1234</div>
    <div><svg width="4" height="4" viewBox="0 0 10 10"><rect y="2" width="10" height="6" fill="#e05a2b"/></svg>info@corvelleng.com</div>
    <div><svg width="4" height="4" viewBox="0 0 10 10"><circle cx="5" cy="5" r="4" fill="none" stroke="#e05a2b" stroke-width="1.6"/></svg>www.corvelleng.com</div>
  </div>
  <div class="letter">
    <p>Dear customer,</p>
    <p style="margin-top:7px">Lorem ipsum dolor sit amet, consectetur adipisicing elit, sed do eiusmod tempor incididunt ut labore et dolore magna aliqua. Ut enim ad minim veniam, quis nostrud exercitation ullamco laboris nisi ut aliquip ex ea commodo consequat. Duis aute irure dolor in reprehenderit in voluptate velit esse cillum dolore eu fugiat nulla pariatur. Excepteur sint occaecat cupidatat non proident, sunt in culpa qui officia deserunt mollit anim id est laborum.</p>
    <p>Lorem ipsum dolor sit amet, consectetur adipisicing elit, sed do eiusmod tempor incididunt ut labore et dolore magna aliqua. Ut enim ad minim veniam, quis nostrud exercitation ullamco laboris nisi ut aliquip ex ea commodo consequat. Duis aute irure dolor in reprehenderit in voluptate velit esse cillum dolore eu fugiat nulla pariatur. Excepteur sint occaecat cupidatat non proident, sunt in culpa qui officia deserunt mollit anim id est laborum.</p>
    <p>Lorem ipsum dolor sit amet, consectetur adipisicing elit, sed do eiusmod tempor incididunt ut labore et dolore magna aliqua. Ut enim ad minim veniam, quis nostrud exercitation ullamco laboris nisi ut aliquip ex ea commodo consequat. Duis aute irure dolor in reprehenderit in voluptate velit esse cillum dolore eu fugiat nulla pariatur. Excepteur sint occaecat cupidatat non proident, sunt in culpa qui officia deserunt mollit anim id est laborum.</p>
    <p>Lorem ipsum dolor sit amet, consectetur adipisicing elit, sed do eiusmod tempor incididunt ut labore et dolore magna aliqua. Ut enim ad minim veniam, quis nostrud exercitation ullamco laboris nisi ut aliquip ex ea commodo consequat. Duis aute irure dolor in reprehenderit.</p>
    <p style="margin-top:6px">Yours Sincerely,</p>
  </div>
  <svg class="signature" width="34" height="32" viewBox="0 0 34 32" aria-hidden="true"><path d="M2 10c4-2 8 2 8 8s-2 12-1 12M9 16c3-4 6-2 6 2s3 2 5-2 2-10 3-10-1 14 2 14 4-6 5-8" fill="none" stroke="#222" stroke-width="0.8"/></svg>
</section>

<!-- presentation folder -->
<section class="piece folder">
  <div class="spine"></div>
  <div class="brand">
    <div class="wordmark">CORVELL ENGINEERING</div>
    <div class="tagline">1420 BRAMBLE RIDGE ROAD, CEDAR FALLS, TEXAS 77000</div>
    <div class="reg">STATE FIRM REGISTRATION F-0412</div>
  </div>
  <div class="photo" role="img" aria-label="Photo of young engineers working together on a red machine in a workshop"></div>
  <div class="footer">
    <div class="company">Corvell Engineering Ltd.</div>
    <div>Unit 12/48 Harlow Lane Brunswick, Victoria Australia</div>
    <div>www.corvelleng.com</div>
  </div>
</section>

<!-- business card back -->
<section class="piece card-back">
  <div class="pattern" role="img" aria-label="Repeating brand pattern on blue"></div>
  <div class="brand">
    <div class="wordmark">CORVELL ENGINEERING</div>
  </div>
</section>

<!-- business card front -->
<section class="piece card-front">
  <div class="brand">
    <div class="wordmark">CORVELL ENGINEERING</div>
    <div class="tagline">1420 BRAMBLE RIDGE ROAD, CEDAR FALLS, TEXAS 77000</div>
    <div class="reg">STATE FIRM REGISTRATION F-0412</div>
  </div>
  <div class="rule"></div>
  <div class="details contact">
    <div class="name">NORTHGATE STUDIO</div>
    <div class="role">Managing Director</div>
    <div style="margin-top:3px">Unit 12/48 Harlow Lane</div>
    <div>Brunswick, Victoria</div>
    <div>Australia</div>
    <div style="margin-top:2px"><svg width="3" height="3" viewBox="0 0 10 10"><path d="M2 1l2 2-1 2 2 2 2-1 2 2-2 2C4 10 0 6 0 3z" fill="#e05a2b"/></svg>+61 3 9000 1234</div>
    <div><svg width="3" height="3" viewBox="0 0 10 10"><rect y="2" width="10" height="6" fill="#e05a2b"/></svg>info@corvelleng.com</div>
    <div><svg width="3" height="3" viewBox="0 0 10 10"><circle cx="5" cy="5" r="4" fill="none" stroke="#e05a2b" stroke-width="1.6"/></svg>www.corvelleng.com</div>
  </div>
</section>

<!-- envelope front -->
<section class="piece envelope-front">
  <div class="ghost" style="left:215px;top:20px;width:110px;height:110px"></div>
  <div class="brand">
    <div class="wordmark">CORVELL ENGINEERING</div>
    <div class="tagline">1420 BRAMBLE RIDGE ROAD, CEDAR FALLS, TEXAS 77000</div>
    <div class="reg">STATE FIRM REGISTRATION F-0412</div>
  </div>
  <div class="sender contact">
    <div class="company">Corvell Engineering Ltd.</div>
    <div>Unit 12/48 Harlow Lane</div>
    <div>Brunswick, Victoria Australia</div>
  </div>
</section>

<!-- envelope back -->
<section class="piece envelope-back">
  <svg class="flap" viewBox="0 0 328 56" aria-hidden="true"><path d="M0 0h328l-5 52q-1 3-5 3H11q-4 0-5-3z" fill="#1f5f99"/></svg>
  <div class="brand">
    <div class="wordmark">CORVELL ENGINEERING</div>
    <div class="tagline">1420 BRAMBLE RIDGE ROAD, CEDAR FALLS, TEXAS 77000</div>
  </div>
</section>

<!-- email signature -->
<section class="piece email-sig">
  <div class="ghost" style="left:215px;top:20px;width:70px;height:70px"></div>
  <div class="brand">
    <div class="wordmark">CORVELL ENGINEERING</div>
    <div class="tagline">1420 BRAMBLE RIDGE ROAD, CEDAR FALLS, TEXAS 77000</div>
    <div class="reg">STATE FIRM REGISTRATION F-0412</div>
  </div>
  <div class="person">
    <div class="name">MARTIN HALE</div>
    <div class="role">Managing Director</div>
  </div>
  <div class="contact-list contact">
    <div><svg width="6" height="6" viewBox="0 0 10 10"><path d="M2 1l2 2-1 2 2 2 2-1 2 2-2 2C4 10 0 6 0 3z" fill="#e05a2b"/></svg>+1 555 014 2290</div>
    <div><svg width="6" height="6" viewBox="0 0 10 10"><rect y="2" width="10" height="6" fill="#e05a2b"/></svg>info@corvelleng.com</div>
    <div><svg width="6" height="6" viewBox="0 0 10 10"><circle cx="5" cy="5" r="4" fill="none" stroke="#e05a2b" stroke-width="1.6"/></svg>www.corvelleng.com</div>
  </div>
  <div class="office">
    <div class="company">Corvell Engineering Ltd.</div>
    <div>48 Willow Crest Road</div>
    <div>Oakridge, ON L0A 1B0</div>
  </div>
</section>

</body>
</html>
```